The Online Growth Blueprint for Garden & Patio Building Crews

We need a book cover design that is for a book targeting landscape and outdoor living contractors that helps them grow their business using online marketing.

We run a business focused on this industry so you can see what we do: https://gardencrewpromo.com/

The title is: The Online Growth Blueprint for Garden & Patio Building Crews

The author is: Trent Halvorsen
Some drafts have been done however they're still looking basic and somewhat amateur, we're looking for something that will stand out.

Target Market(s)

Landscape, Hardscape and Outdoor Living Contractors and Business Owners

Industry/Entity Type

Online Marketing

Font styles to use
Serif
Sans Serif

Requirements
Must have
• The part of the title that should stand out the most is the text "Online Growth Blueprint".
Should not have
• The color red

```html
<!DOCTYPE html>
<html lang="en">
<head>
<meta charset="utf-8">
<title>The Online Growth Blueprint for Garden &amp; Patio Building Crews — Book Cover</title>
<link rel="stylesheet" href="https://fonts.googleapis.com/css2?family=Oswald:wght@500;600;700&display=swap">
<style>
  :root {
    --stage: #5f5f5f;
    --navy: #1e2734;
    --lime: #a4c81b;
    --white: #ffffff;
    --leaf: #6f8f4a;
    --leaf-light: #a9bf8c;
    --deck: #7d8689;
  }
  * { margin: 0; padding: 0; box-sizing: border-box; }
  html, body {
    width: 1200px;
    height: 893px;
    overflow: hidden;
    background: var(--stage);
  }
  .canvas {
    position: relative;
    width: 1200px;
    height: 893px;
  }
  .cover {
    position: absolute;
    left: 336px;
    top: 26px;
    width: 528px;
    height: 840px;
    background: var(--navy);
    font-family: "Oswald", "Arial Narrow", sans-serif;
    color: var(--white);
    text-align: center;
    overflow: hidden;
  }
  .publisher {
    position: absolute;
    top: 62px;
    left: 0;
    right: 0;
    display: flex;
    justify-content: center;
    align-items: center;
    gap: 10px;
    font-weight: 600;
    font-size: 17px;
    letter-spacing: 0.5px;
    text-transform: uppercase;
    color: var(--lime);
  }
  .publisher-mark {
    width: 14px;
    height: 14px;
    background: var(--lime);
  }
  .title {
    position: absolute;
    top: 140px;
    left: 0;
    right: 0;
    text-transform: uppercase;
    line-height: 1;
  }
  .title-lead {
    display: block;
    font-weight: 700;
    font-size: 30px;
    color: var(--white);
  }
  .title-kicker {
    display: block;
    margin-top: 4px;
    font-weight: 700;
    font-size: 43px;
    color: var(--lime);
  }
  .title-main {
    display: block;
    margin-top: 2px;
    font-weight: 700;
    font-size: 74px;
    letter-spacing: 0.5px;
    color: var(--lime);
  }
  .title-sub {
    display: block;
    margin-top: 6px;
    font-weight: 600;
    font-size: 28px;
    line-height: 1.15;
    color: var(--white);
  }
  .scene {
    position: absolute;
    left: 0;
    top: 366px;
    width: 528px;
    height: 354px;
  }
  .rule {
    position: absolute;
    left: 0;
    top: 718px;
    width: 528px;
    height: 9px;
    background: var(--lime);
  }
  .author {
    position: absolute;
    left: 0;
    right: 0;
    top: 748px;
    font-weight: 700;
    font-size: 50px;
    line-height: 1;
    text-transform: uppercase;
    color: var(--white);
  }
</style>
</head>
<body>
  <main class="canvas">
    <article class="cover">
      <div class="publisher">
        <span class="publisher-mark"></span>
        <span class="publisher-name">Yardline Contractor Growth</span>
      </div>

      <h1 class="title">
        <span class="title-lead">The</span>
        <span class="title-kicker">Online Growth</span>
        <span class="title-main">Blueprint</span>
        <span class="title-sub">For Garden &amp; Patio<br>Building Crews</span>
      </h1>

      <svg class="scene" viewBox="0 0 528 354" role="img" aria-label="Photo of a backyard with a wooden gazebo, deck boardwalk, willow trees and flower beds">
        <defs>
          <linearGradient id="sceneTone" x1="0" y1="0" x2="0" y2="1">
            <stop offset="0" stop-color="#c9d6b6"/>
            <stop offset="0.35" stop-color="#6f8f4a"/>
            <stop offset="0.7" stop-color="#8a9294"/>
            <stop offset="1" stop-color="#6d7475"/>
          </linearGradient>
        </defs>
        <path fill="url(#sceneTone)" d="M0 30 L18 24 L34 30 L52 20 L70 26 L92 18 L110 24 L128 14 L150 22 L170 16 L188 24 L206 12 L226 20 L248 10 L266 18 L288 8 L306 16 L326 6 L346 14 L366 4 L384 12 L404 2 L424 10 L444 0 L462 8 L480 2 L500 10 L516 4 L528 8 L528 354 L0 354 Z"/>
      </svg>

      <div class="rule"></div>

      <p class="author">Trent Halvorsen</p>
    </article>
  </main>
</body>
</html>
```